Attractive Flyer for Moving Company

Our Company is called "Harborline Haulers".
We provide moving service for home and businesses
We need a flyer for a moving company, located in South Florida USA
Flyer size will be 7 x 5 inches, double sided.

Flyer needs to be very attractive and catchy for eye. I want people to keep it even if they don't need our service. I attached a lot of text in separate word file.
Logo, brief and additional pictures are attached.

```html
<!DOCTYPE html>
<html lang="en">
<head>
<meta charset="utf-8">
<title>Harborline Haulers – Moving Flyer</title>
<link rel="stylesheet" href="https://fonts.googleapis.com/css2?family=Montserrat:wght@700;800;900&family=Questrial&display=swap">
<style>
  :root{
    --red:#e3141b;
    --ink:#111111;
    --text:#2a2a2a;
    --white:#ffffff;
    --stage:#c9c9c9;
    --photo-a:#d9d4cc;
    --photo-b:#9c8a72;
    --room-a:#e6e3de;
    --room-b:#a9a39a;
  }
  *{box-sizing:border-box;margin:0;padding:0}
  html,body{width:1200px;height:1200px;overflow:hidden}
  body{background:var(--stage);font-family:"Questrial",sans-serif;color:var(--text);position:relative}
  .flyer{position:absolute;width:557px;height:780px;background:var(--white);overflow:hidden;box-shadow:0 6px 18px rgba(0,0,0,.25)}
  .flyer--front{left:25px;top:210px}
  .flyer--back{left:615px;top:206px;height:778px}
  .photo{position:absolute;left:0;top:0}
  .brand{position:absolute;display:flex;align-items:center;gap:7px}
  .brand__mark{width:13px;height:13px;background:var(--red);border-radius:50%}
  .brand__name{font-family:"Montserrat",sans-serif;font-weight:900;font-size:22px;color:var(--red);letter-spacing:-.2px}
  .headline{position:absolute;left:26px;top:348px;font-size:29px;font-weight:400;color:var(--red)}
  .license{position:absolute;left:26px;top:385px;font-size:14.5px;line-height:18px;color:var(--ink)}
  .soon{position:absolute;left:26px;top:431px;font-family:"Montserrat",sans-serif;font-weight:900;font-size:36px;color:var(--ink);letter-spacing:.5px}
  .note{position:absolute;left:26px;top:474px;font-size:13px;line-height:17px;color:var(--ink);white-space:nowrap}
  .badge-round{position:absolute;left:406px;top:451px;width:48px;height:48px;border-radius:50%;background:#b8241d}
  .badge-square{position:absolute;left:476px;top:453px;width:26px;height:42px;background:#1b5fa7;border-radius:2px}
  .bar{position:absolute;background:var(--red);color:var(--white);font-family:"Montserrat",sans-serif;font-weight:800;display:flex;align-items:center;white-space:nowrap}
  .bar--why{left:0;top:512px;width:158px;height:26px;font-size:17px;padding-left:26px}
  .bar--services{left:339px;top:512px;width:178px;height:26px;font-size:16.5px;padding-left:13px}
  .list{position:absolute;list-style:none}
  .list li{position:relative;padding-left:16px}
  .list li::before{content:"";position:absolute;left:0;width:8px;height:8px;border-radius:50%;background:var(--red)}
  .list--why{left:26px;top:547px;width:290px;font-size:13.5px;line-height:18.7px;color:var(--ink)}
  .list--why li::before{top:5px}
  .list--services{left:351px;top:545px;width:200px;font-size:15.5px;line-height:20.5px;color:var(--ink)}
  .list--services li::before{top:6px}
  .contact{position:absolute;left:0;width:100%;height:53px;background:var(--red);color:var(--white);display:flex}
  .flyer--front .contact{top:718px}
  .flyer--back .contact{top:715px}
  .contact__cell{padding:3px 0 0 35px;position:relative;white-space:nowrap}
  .contact__cell--phone{width:249px}
  .contact__cell--web{flex:1;border-left:1.5px solid rgba(255,255,255,.8);padding-left:32px;margin:4px 0}
  .contact__label{font-size:15px;line-height:19px}
  .contact__value{display:flex;align-items:center;gap:9px;font-size:18px;line-height:26px;letter-spacing:.3px}
  .contact__cell--web .contact__value{font-size:16.5px;letter-spacing:0}
  .contact__value svg{flex:none}
  .bar--deal{left:0;top:380px;width:197px;height:28px;font-size:18px;padding-left:24px}
  .bar--included{left:0;top:570px;width:178px;height:26px;font-family:"Questrial",sans-serif;font-weight:400;font-size:15px;padding-left:23px}
  .list--deal{left:24px;top:419px;width:415px;font-size:19px;line-height:24px;color:var(--ink);letter-spacing:.3px}
  .list--deal li::before{top:8px}
  .list--deal strong{color:var(--red);font-family:"Montserrat",sans-serif;font-weight:800}
  .list--included{left:24px;top:606px;width:520px;font-size:15px;line-height:23px;color:var(--ink)}
  .list--included li::before{top:7px}
  .voucher{position:absolute;left:41px;top:678px;font-family:"Montserrat",sans-serif;font-weight:800;font-size:18px;color:var(--red);white-space:nowrap}
</style>
</head>
<body>

<section class="flyer flyer--front">
  <svg class="photo" width="557" height="400" viewBox="0 0 557 400" role="img" aria-label="Photo of two movers in blue uniforms unloading cardboard boxes from a white van">
    <defs>
      <linearGradient id="vanPhoto" x1="0" y1="0" x2="1" y2="1">
        <stop offset="0" stop-color="var(--photo-a)"/>
        <stop offset=".55" stop-color="#b9a58a"/>
        <stop offset="1" stop-color="var(--photo-b)"/>
      </linearGradient>
      <linearGradient id="housePhoto" x1="0" y1="0" x2="0" y2="1">
        <stop offset="0" stop-color="#a9c3a0"/>
        <stop offset="1" stop-color="#6f8e55"/>
      </linearGradient>
    </defs>
    <path d="M0 0H557V262Q300 372 0 302Z" fill="url(#vanPhoto)"/>
    <path d="M0 302Q300 372 557 262V280Q300 392 0 318Z" fill="var(--red)"/>
    <circle cx="429" cy="275" r="80" fill="url(#housePhoto)" stroke="var(--red)" stroke-width="4"/>
  </svg>

  <div class="brand" style="left:18px;top:40px">
    <span class="brand__mark"></span><span class="brand__name">Harborline Haulers</span>
  </div>

  <h1 class="headline">Where Speed Meets Quality</h1>
  <p class="license">Licensed &amp; Fully Insured, FL MOVERS LICENSE#:<br>IM5521 US DOT: #4417290</p>
  <h2 class="soon">MOVING SOON</h2>
  <p class="note">Not moving soon? Keep this flyer for later and/or share it<br>with friends. Promotion is valid until January 1<sup style="font-size:7px">st</sup>, 2020)</p>
  <span class="badge-round"></span>
  <span class="badge-square"></span>

  <div class="bar bar--why">Why Call Us?</div>
  <div class="bar bar--services">Moving Services:</div>

  <ul class="list list--why">
    <li>Customer Service Oriented</li>
    <li>Years of Great reputation (Lots of 5 Star Reviews)</li>
    <li>Affordable pricing</li>
    <li>Professional, efficient, strong movers</li>
    <li>We always handle your belongings with care</li>
    <li>Clean and equipped trucks</li>
    <li>Absolutely NO hidden fees</li>
  </ul>
  <ul class="list list--services">
    <li>Residential,</li>
    <li>Long Distance,</li>
    <li>Commercial,</li>
    <li>Loading / Unloading<br>rental truck /<br>portable storage,</li>
    <li style="margin-top:4px">Packing Service</li>
  </ul>

  <footer class="contact">
    <div class="contact__cell contact__cell--phone">
      <div class="contact__label">Call For A Quick Estimate</div>
      <div class="contact__value">
        <svg width="20" height="20" viewBox="0 0 20 20"><circle cx="10" cy="10" r="9" fill="none" stroke="#fff" stroke-width="1.5"/><path d="M7 5.5l2 2-1 1.3c.6 1.3 1.6 2.3 2.9 2.9l1.3-1 2 2-1.3 1.4C9.8 14 6 10.2 5.8 6.8Z" fill="#fff"/></svg>
        (800) 555-0148
      </div>
    </div>
    <div class="contact__cell contact__cell--web">
      <div class="contact__label">Request Your Estimate online</div>
      <div class="contact__value">
        <svg width="18" height="18" viewBox="0 0 18 18" fill="none" stroke="#fff" stroke-width="1.4"><circle cx="9" cy="9" r="8"/><ellipse cx="9" cy="9" rx="3.5" ry="8"/><path d="M1 9h16M2.5 5h13M2.5 13h13"/></svg>
        www.harborlinehaulers.com
      </div>
    </div>
  </footer>
</section>

<section class="flyer flyer--back">
  <svg class="photo" width="557" height="400" viewBox="0 0 557 400" role="img" aria-label="Photo of a happy couple playing with a cardboard moving box in a bright living room">
    <defs>
      <linearGradient id="roomPhoto" x1="0" y1="0" x2="1" y2="1">
        <stop offset="0" stop-color="var(--room-a)"/>
        <stop offset=".6" stop-color="#bdb8b0"/>
        <stop offset="1" stop-color="var(--room-b)"/>
      </linearGradient>
    </defs>
    <path d="M0 0H557V305Q360 400 0 290Z" fill="url(#roomPhoto)"/>
    <path d="M0 290Q360 400 557 305V318Q360 414 0 304Z" fill="var(--red)"/>
  </svg>

  <div class="brand" style="left:25px;top:48px">
    <span class="brand__mark"></span><span class="brand__name">Harborline Haulers</span>
  </div>

  <div class="bar bar--deal">Your Special Deal</div>
  <ul class="list list--deal">
    <li>SAVE <strong>15% -25%</strong> on your move</li>
    <li><strong>$275</strong> – 3 hours of Moving Service with 2 PRO<br>MOVERS</li>
    <li><strong>$325</strong> - 3 hours of Moving Service with 3 PRO<br>MOVERS</li>
    <li><strong>+ 20% OFF</strong> boxes and packing supplies.</li>
  </ul>

  <div class="bar bar--included">INCLUDED IN PRICE</div>
  <ul class="list list--included">
    <li>Protection of your furniture with specialized blankets and plastic wrap.</li>
    <li>Disassembly and reassembly of your furniture.</li>
    <li>Wardrobe boxes for the duration of moving process.</li>
  </ul>

  <p class="voucher">Keep this voucher, it is valid until January 1<sup style="font-size:9px">st</sup>, 2020</p>

  <footer class="contact">
    <div class="contact__cell contact__cell--phone">
      <div class="contact__label">Call For A Quick Estimate</div>
      <div class="contact__value">
        <svg width="20" height="20" viewBox="0 0 20 20"><circle cx="10" cy="10" r="9" fill="none" stroke="#fff" stroke-width="1.5"/><path d="M7 5.5l2 2-1 1.3c.6 1.3 1.6 2.3 2.9 2.9l1.3-1 2 2-1.3 1.4C9.8 14 6 10.2 5.8 6.8Z" fill="#fff"/></svg>
        (800) 555-0148
      </div>
    </div>
    <div class="contact__cell contact__cell--web">
      <div class="contact__label">Request Your Estimate online</div>
      <div class="contact__value">
        <svg width="18" height="18" viewBox="0 0 18 18" fill="none" stroke="#fff" stroke-width="1.4"><circle cx="9" cy="9" r="8"/><ellipse cx="9" cy="9" rx="3.5" ry="8"/><path d="M1 9h16M2.5 5h13M2.5 13h13"/></svg>
        www.harborlinehaulers.com
      </div>
    </div>
  </footer>
</section>

</body>
</html>
```